Stationary mockup / corporate identity stationary presentation

We have developed a business card, envelope, and so on. We want to use a stationary mock up for internal presentation using a mock up template. The idea behind the logo is OK, we do not want to change, but we want to look for some creativity, we have a business card, letter head stationary, complements card, evenloppe etc. For mock up example templates, please look at: https://plumvexa.com/free-brandingidentity-stationery-psd-mockups/ We include the logo as word document. There are two logo's similar but differnet colors and name. These represent two activities within the same group company. For both we want to have a presentation and be stationary mock up. What we need is a complete presentation of different corporate identity items as a business card, envelope, letterhead stationary, compliments cards, pen, muck, etc. etc. mock up or please check: https: // plumvexa. com / free-brandingidentity-stationery-psd-mockups / http://www.gordalune.com/index.php?site=forum_topic&topic=1 Please look at website: http://www.tomselvikora.com/marquet/ This is sister website. For VILMORE will be the same.

Industry/Entity Type

Architecture

Font styles to use
Sans Serif

Colors
33a6d7

Requirements
Must have
• Please look at website: http://www.tomselvikora.com/marquet/ This is sister website. For VILMORE will be the same. How if you want. We want to search for uniformity in website and stationary design. But are open for suggestions offcourse.
Nice to have

```html
<!DOCTYPE html>
<html lang="en">
<head>
<meta charset="utf-8">
<title>Vilmore Architectures – Stationery Set</title>
<link href="https://fonts.googleapis.com/css2?family=Arimo:wght@400;700&family=Raleway:wght@300;400&display=swap" rel="stylesheet">
<style>
  :root {
    --bg: #e3e3e3;
    --paper: #f4f4f4;
    --paper-white: #ffffff;
    --brand-blue: #4a90e2;
    --folder-panel: #5b9de4;
    --ink: #111111;
    --ink-soft: #555555;
    --rule: #b8b8b8;
  }
  * { box-sizing: border-box; margin: 0; padding: 0; }
  html, body { width: 1200px; height: 816px; overflow: hidden; background: var(--bg); }
  .canvas { position: relative; width: 1200px; height: 816px; background: var(--bg); font-family: "Arimo", Arial, sans-serif; color: var(--ink); }

  .sheet { position: absolute; background: var(--paper); box-shadow: 0 1px 3px rgba(0,0,0,.18); }

  /* brand name set as plain text */
  .wordmark { position: absolute; white-space: nowrap; font-weight: 400; color: var(--ink); line-height: 1; }
  .wordmark .word + .word { margin-left: .7em; }
  .wordmark.on-blue { color: #fff; }

  /* contact block */
  .contact { position: absolute; font-size: 5px; line-height: 7px; color: var(--ink-soft); padding-left: 8px; border-left: 1px solid var(--rule); font-style: normal; }
  .contact .gap { height: 4px; }
  .contact .line { display: flex; align-items: center; }
  .contact .icon { width: 3.5px; height: 3.5px; background: var(--brand-blue); border-radius: 50%; margin-right: 4px; flex: none; }

  /* letterhead */
  .letterhead { left: 250px; top: 78px; width: 344px; height: 483px; }
  .letter-greeting { position: absolute; left: 31px; top: 138px; font-family: "Raleway", sans-serif; font-size: 8px; color: #333; }
  .letter-body { position: absolute; left: 31px; top: 162px; width: 285px; font-family: "Raleway", sans-serif; font-size: 4.4px; line-height: 7.3px; color: #555; }
  .letter-body p { margin-bottom: 7.3px; }

  /* folder */
  .folder { left: 624px; top: 48px; width: 406px; height: 513px; background: var(--brand-blue); }
  .folder-spine { position: absolute; top: 0; bottom: 0; width: 1px; background: rgba(255,255,255,.35); }
  .folder-panel { position: absolute; left: 26px; top: 19px; width: 362px; height: 352px; background: var(--folder-panel); }

  /* business cards */
  .card-front { left: 64px; top: 378px; width: 143px; height: 82px; background: var(--paper-white); }
  .card-back { left: 64px; top: 475px; width: 143px; height: 81px; background: var(--brand-blue); }
  .card-person { position: absolute; left: 84px; top: 19px; font-size: 3.3px; line-height: 4.4px; color: var(--ink-soft); padding-left: 4px; border-left: .5px solid var(--rule); }
  .card-person .name { font-size: 5px; font-weight: 700; color: var(--brand-blue); line-height: 5px; }
  .card-person .role { font-weight: 700; color: var(--ink); margin-bottom: 3px; }
  .card-person .icon { display: inline-block; width: 2.4px; height: 2.4px; border-radius: 50%; background: var(--brand-blue); margin-right: 2px; }
  .card-url { position: absolute; left: 0; right: 0; bottom: 9px; text-align: center; font-size: 3px; letter-spacing: 2.2px; color: rgba(255,255,255,.85); }

  /* envelope */
  .envelope { left: 62px; top: 596px; width: 396px; height: 180px; }
  .envelope-address { position: absolute; left: 29px; top: 45px; font-size: 7px; color: #333; }

  /* compliments slip */
  .compliments { left: 477px; top: 595px; width: 396px; height: 180px; }
  .compliments-title { position: absolute; left: 239px; top: 134px; font-family: "Raleway", sans-serif; font-weight: 300; font-size: 14.5px; color: var(--brand-blue); }
</style>
</head>
<body>
<main class="canvas">

  <section class="sheet letterhead">
    <div class="wordmark" style="left:33px; top:57px; font-size:8.5px;"><span class="word">VILMORE</span><span class="word">architectures</span></div>
    <address class="contact" style="left:252px; top:28px;">
      <div>4120 Larkfield Row</div>
      <div>Brenmoor, Ostara 51208</div>
      <div class="gap"></div>
      <div class="line"><span class="icon"></span>512 830 4471</div>
      <div class="line"><span class="icon"></span>604 219 7785</div>
      <div class="line"><span class="icon"></span>mail@vilmore-arch.com</div>
      <div class="line"><span class="icon"></span>www.vilmore-arch.com</div>
    </address>
    <p class="letter-greeting">Dear Mr. Prewitt,</p>
    <div class="letter-body">
      <p>Thank you for meeting with our team last week to discuss the riverside library project. We have reviewed the site notes, the zoning limits and the early budget, and we believe a light timber frame with a glazed reading hall suits both the brief and the schedule.</p>
      <p>Enclosed you will find the first sketch package, a short list of material options and a draft programme of works. Each option keeps the public entrance on the square and leaves room for a later extension to the east.</p>
      <p>We would welcome your comments before the next review. If it helps, our project lead can visit your office to walk through the drawings and answer questions from the board.</p>
      <p>Thank you again for your trust in our studio.</p>
      <p style="margin-top:11px;">Sincerely,</p>
    </div>
  </section>

  <section class="sheet folder">
    <span class="folder-spine" style="left:9px;"></span>
    <span class="folder-spine" style="left:13px;"></span>
    <span class="folder-spine" style="left:22px;"></span>
    <div class="folder-panel"></div>
    <div class="wordmark on-blue" style="left:48px; top:426px; font-size:24px;"><span class="word">VILMORE</span><span class="word">architectures</span></div>
  </section>

  <section class="sheet card-front">
    <div class="wordmark" style="left:12px; top:39px; font-size:4px;"><span class="word">VILMORE</span><span class="word">architectures</span></div>
    <div class="card-person">
      <div class="name">ALDEN PREWITT</div>
      <div class="role">CEO/FOUNDER</div>
      <div>4120 Larkfield Row</div>
      <div>Brenmoor, Ostara 51208</div>
      <div><span class="icon"></span>512 830 4471</div>
      <div><span class="icon"></span>604 219 7785</div>
      <div><span class="icon"></span>433 702 5518</div>
      <div><span class="icon"></span>mail@vilmore-arch.com</div>
      <div><span class="icon"></span>www.vilmore-arch.com</div>
    </div>
  </section>

  <section class="sheet card-back">
    <div class="card-url">www.vilmore-arch.com</div>
  </section>

  <section class="sheet envelope">
    <div class="wordmark" style="left:27px; top:30px; font-size:12.5px;"><span class="word">VILMORE</span><span class="word">architectures</span></div>
    <div class="envelope-address">4120 Larkfield Row, Brenmoor, Ostara 51208</div>
  </section>

  <section class="sheet compliments">
    <div class="wordmark" style="left:22px; top:31px; font-size:8.5px;"><span class="word">VILMORE</span><span class="word">architectures</span></div>
    <address class="contact" style="left:303px; top:17px;">
      <div>4120 Larkfield Row</div>
      <div>Brenmoor, Ostara 51208</div>
      <div class="gap"></div>
      <div class="line"><span class="icon"></span>512 830 4471</div>
      <div class="line"><span class="icon"></span>604 219 7785</div>
      <div class="line"><span class="icon"></span>mail@vilmore-arch.com</div>
      <div class="line"><span class="icon"></span>www.vilmore-arch.com</div>
    </address>
    <p class="compliments-title">With Compliments</p>
  </section>

</main>
</body>
</html>
```